Charity donation cards

I need a card in an envelope that would be given out to people and they would put their donations along with their details (name and email) and give it back to us (dropped in acrylic boxes at events etc).

The card should be a medium size, bi or tri fold to be able to fit all the information i require.

The Sarwa Fund

The Bright Meadow Centre is dedicated to providing the much needed support to families and children struggling with their differences through a holistic and comprehensive approach that includes detailed evaluations, therapy programs and support services to help unlock the potential in every child.

We are so proud to be able to help empower our society by dedicating our business to the mental, physical and social well being of our younger community and pledging all our net profits to help ensure no child is ever left behind.

Professional services can often be expensive. Our Sarwa Fund helps support families requiring financial aid. We believe every child deserves the opportunity to succeed and no child should be left behind.

How can you help?

Gift the therapies to the children that need it the most. We welcome new sponsors, appreciate your gifts and gratefully accept your contributions as we expand to increase the number of children we can serve.

Name:
Email:
Amount:

We accept cash, checks or credit card payments at The Bright Meadow Centre.

Gift cards should be dropped in the designated acrylic boxes at TBMC or the event.

Please email sarwafund@kovelmint.ae for more information on the process.
Http://www.kovelmint.ae

Target Market(s)

These cards will be placed in the reception for our clients to donate.

We will also be working with party planners. Some parents don't want people to get them gifts for their kids birthday party so they want to use this instead.

Industry/Entity Type

Charity

Requirements
Must have
• The same feel as our centre Http://www.kovelmint.ae
• our website, email and contact number
Nice to have
• Go to our website and feel free to take ideas and content.
• The design should be clean and simple.
• High light the key words in the text with bold and maybe in green to make it pop out.
Should not have
• Do not use the word donate in any print material. The word should be gift.

```html
<!DOCTYPE html>
<html lang="en">
<head>
<meta charset="utf-8">
<title>The Sarwa Fund – Gift Card Set</title>
<link href="https://fonts.googleapis.com/css2?family=Poiret+One&display=swap" rel="stylesheet">
<style>
  :root {
    --paper: #ffffff;
    --backdrop: #ffffff;
    --ink: #3a3a3a;
    --ink-soft: #6a6a6a;
    --charcoal: #3c3d3f;
    --edge: #d9d9d9;
    --blue: #1aa3e0;
    --orange: #ef6f1f;
    --pink: #f07cb8;
    --green: #4cb848;
    --peach: #f9c99a;
    --yellow: #f6a623;
    --brown: #8a4b12;
    --red: #e8392e;
    --violet: #5b3fa0;
    --body: "Poiret One", "Century Gothic", sans-serif;
  }
  * { box-sizing: border-box; margin: 0; padding: 0; }
  html, body { width: 1200px; height: 1000px; overflow: hidden; background: var(--backdrop); }
  body { position: relative; font-family: var(--body); color: var(--ink); }

  .piece { position: absolute; background: var(--paper); box-shadow: 0 2px 10px rgba(0,0,0,.18); }

  /* Front of the card */
  .card-front { left: 55px; top: 60px; width: 550px; height: 425px; overflow: hidden; }
  .brand { position: absolute; left: 140px; top: 135px; display: flex; align-items: center; gap: 16px; }
  .brand-dot { width: 34px; height: 34px; border-radius: 50%; background: var(--orange); }
  .brand-name { font-family: var(--body); font-size: 40px; font-weight: 400; color: var(--ink-soft); line-height: 1; }
  .front-swoosh { position: absolute; left: 0; top: 220px; width: 550px; height: 205px; }
  .front-message { position: absolute; left: 60px; right: 60px; top: 330px; text-align: center; font-size: 14.5px; line-height: 1.6; color: var(--ink); }

  /* Envelope */
  .envelope { left: 55px; top: 515px; width: 555px; height: 425px; overflow: hidden; }
  .envelope svg { width: 100%; height: 100%; display: block; }

  /* Inside of the card */
  .card-inside { left: 620px; top: 115px; width: 515px; height: 760px; overflow: hidden; }
  .ribbon-top { position: absolute; left: 0; top: 0; width: 100%; height: 95px;
    background: linear-gradient(100deg, var(--blue) 0%, var(--pink) 25%, var(--orange) 50%, var(--green) 72%, var(--yellow) 100%);
    clip-path: polygon(0 0, 100% 0, 100% 35%, 70% 55%, 40% 80%, 0 100%); opacity: .9; }
  .ribbon-bottom { position: absolute; right: 0; bottom: 0; width: 100%; height: 150px;
    background: linear-gradient(280deg, var(--blue) 0%, var(--pink) 25%, var(--orange) 50%, var(--green) 72%, var(--peach) 100%);
    clip-path: polygon(100% 0, 100% 100%, 0 100%, 20% 80%, 55% 45%); opacity: .9; }

  .inside-text { position: absolute; left: 22px; right: 26px; top: 52px; font-size: 13.5px; line-height: 1.5; color: var(--ink); }
  .inside-text h2 { font-size: 14px; font-weight: 400; text-align: center; margin-bottom: 22px; padding-left: 60px; }
  .inside-text h3 { font-size: 14px; font-weight: 400; text-align: center; margin: 30px 0 18px; }
  .inside-text p { text-align: justify; text-indent: 50px; margin-bottom: 20px; }
  .inside-text .fold-gap { height: 4px; }

  .details { list-style: none; margin: 4px 0 26px 40px; }
  .details li { display: flex; font-size: 13.5px; line-height: 1.45; }
  .details .label { width: 56px; text-align: right; padding-right: 10px; }

  .payment { text-align: center; margin-bottom: 10px; }
  .contact { text-align: center; font-size: 13px; line-height: 1.6; position: relative; }
  .contact .lead { color: var(--red); }
  .contact .mail { color: var(--violet); }
  .contact .web { color: var(--green); }
</style>
</head>
<body>

  <section class="piece card-front">
    <div class="brand">
      <span class="brand-dot"></span>
      <span class="brand-name">The Bright Meadow Centre</span>
    </div>
    <svg class="front-swoosh" viewBox="0 0 550 205" aria-hidden="true">
      <path d="M0 60 C 120 110, 230 70, 330 30 C 410 0, 480 20, 548 205" fill="none" stroke="var(--charcoal)" stroke-width="5"/>
    </svg>
    <p class="front-message">Gift the therapies to the children that need it the most. We welcome new sponsors, appreciate your gifts and gratefully accept your contributions as we expand to increase the number of children we can serve.</p>
  </section>

  <section class="piece envelope" aria-label="Envelope">
    <svg viewBox="0 0 555 425" preserveAspectRatio="none">
      <path d="M0 425 L 278 215 L 555 425" fill="none" stroke="var(--edge)" stroke-width="2"/>
      <path d="M0 55 L 250 232 Q 278 250 305 232 L 555 0 L 0 0 Z" fill="var(--charcoal)"/>
    </svg>
  </section>

  <section class="piece card-inside">
    <div class="ribbon-top" role="img" aria-label="Flowing multicolour ribbon decoration"></div>
    <div class="ribbon-bottom" role="img" aria-label="Flowing multicolour ribbon decoration"></div>

    <div class="inside-text">
      <h2>The Sarwa Fund</h2>
      <p>The Bright Meadow Centre is dedicated to providing the much needed support to families and children struggling with their differences through a holistic and comprehensive approach that includes detailed evaluations, therapy programs and support services to help unlock the potential in every child.</p>
      <p>We are so proud to be able to help empower our society by dedicating our business to the mental, physical and social well being of our younger community and pledging all our net profits to help ensure no child is ever left behind.</p>
      <p>Professional services can often be expensive. Our Sarwa Fund helps support families requiring financial aid. We believe every child deserves the opportunity to succeed and no child should be left behind.</p>

      <h3>How can you help?</h3>
      <p>Gift the therapies to the children that need it the most. We welcome new sponsors, appreciate your gifts and gratefully accept your contributions as we expand to increase the number of children we can serve.</p>

      <ul class="details">
        <li><span class="label">Name</span>:</li>
        <li><span class="label">Email</span>:</li>
        <li><span class="label">Amount</span>:</li>
      </ul>

      <p class="payment">We accept cash, checks or credit card payments at The Bright Meadow Centre. Gift cards should be dropped in the designated acrylic boxes at TBMC or the event.</p>
      <div class="contact">
        <span class="lead">Please email</span> <span class="mail">sarwafund@kovelmint.ae</span> <span class="lead">for more information on the process.</span><br>
        <span class="web">Http://www.kovelmint.ae The Sarwa Fund</span>
      </div>
    </div>
  </section>

</body>
</html>
```